Sponsor at Title Insurance Industry Seminar for Continuing Ed - 250 Companies in Attendance

I offer escrow accounting services in the Title Insurance Industry. I've attached logo files and an example of my former company. I don't like the design and it's a little wordy but it provides detail of what I offer.

Below is a brief write-up...
For professionals in the title insurance industry, finding a reliable and cost-effective solution to escrow accounting needs can feel overwhelming. When choosing the right accounting partner, title companies and law firms need a group they can trust, and that’s where we come in. Brightfen Ledger Works is a team that understands the title industry and the importance of compliance, security and accuracy. Brightfen Ledger Works is the experienced, convenient and cost-effective choice for the accounting and certification needs of companies throughout the country.

```html
<!DOCTYPE html>
<html lang="en">
<head>
<meta charset="UTF-8">
<title>Brightfen Ledger Works – Flyer</title>
<link rel="stylesheet" href="https://fonts.googleapis.com/css2?family=Oswald:wght@400;500&family=Poppins:wght@300;400;500;600;700&family=Montserrat:wght@400;500&display=swap">
<style>
  :root{
    --copper:#b8735c;
    --navy:#37404e;
    --ink:#2f3845;
    --mist:#efefef;
    --blush:#ecdcd3;
    --stone:#d6d6da;
    --white:#ffffff;
    --stage:#4b4b4b;
  }
  *{box-sizing:border-box;margin:0;padding:0}
  html,body{width:1200px;height:803px;overflow:hidden}
  body{background:var(--stage);font-family:"Poppins",sans-serif;color:var(--ink);position:relative}
  .flyer{position:absolute;top:104px;width:484px;height:626px;background:var(--white);overflow:hidden}
  .flyer--front{left:82px}
  .flyer--back{left:638px}
  .abs{position:absolute}
  .shapes{position:absolute;left:0;top:0;width:484px;height:626px}

  .web{position:absolute;right:28px;font-size:8px;color:var(--white);letter-spacing:.2px;display:flex;align-items:center;gap:3px}
  .web b{font-weight:600}

  .brand{position:absolute;display:flex;align-items:center;gap:7px}
  .brand__mark{width:24px;height:24px;background:var(--copper)}
  .brand__name{font-weight:600;color:var(--copper);font-size:12px;line-height:13px;letter-spacing:.6px;text-transform:uppercase}

  .headline{left:31px;top:110px;font-family:"Oswald",sans-serif;font-weight:500;font-size:28px;line-height:32px;color:var(--copper);text-transform:uppercase}
  .headline span{color:var(--ink);font-weight:400}
  .lede{left:31px;top:224px;width:190px;border-left:2px solid var(--copper);padding-left:9px;font-weight:600;font-size:12.3px;line-height:14.3px;color:var(--ink)}

  .photo{position:absolute;background:linear-gradient(135deg,#e9eef5,#9fb3cc 55%,#5d6f86)}
  .photo--team{left:262px;top:117px;width:170px;height:168px;border-top-left-radius:40px;border:5px solid var(--white)}
  .photo--desk{left:27px;top:64px;width:429px;height:225px;border-radius:48px 0 82px 0;background:linear-gradient(120deg,#3a3a38,#8e8f8d 40%,#e8e8e6 60%,#6f6e6a)}

  .services{left:31px;top:309px;width:209px;height:210px;background:var(--navy);border-radius:46px 0 46px 0}
  .services__title{position:absolute;left:38px;top:20px;color:var(--white);font-weight:300;font-size:15.5px;letter-spacing:.3px}
  .services__title b{color:var(--copper);font-weight:700}
  .service{position:absolute;left:36px;display:flex;align-items:center;gap:8px}
  .service svg{width:20px;height:20px}
  .service p{border-left:1px solid rgba(255,255,255,.5);padding-left:8px;color:var(--white);font-size:9.2px;line-height:11.3px;font-weight:500}

  .promise{left:51px;top:447px;width:165px;height:70px;border:1px solid var(--copper);border-bottom:none;padding:15px 22px 0 13px;color:var(--white);font-weight:600;font-size:10.4px;line-height:12.6px}
  .score{left:51px;top:517px;width:165px;height:54px;background:var(--copper);clip-path:polygon(0 0,100% 0,100% 70%,88% 100%,0 100%);display:flex;align-items:center;padding-left:10px;color:var(--white)}
  .score__num{font-weight:600;font-size:31px;letter-spacing:-.5px;padding-right:7px;border-right:1px solid rgba(255,255,255,.7);line-height:36px}
  .score__list{padding-left:6px;font-size:7.2px;line-height:10px;font-weight:500;text-transform:uppercase;letter-spacing:.3px}

  .body-copy{font-family:"Montserrat",sans-serif;font-size:9.3px;line-height:12.7px;color:var(--ink)}
  .intro{left:262px;top:328px;width:172px}
  .pull{left:262px;top:509px;width:180px;border-left:2px solid var(--copper);padding-left:10px;font-weight:600;font-size:12.3px;line-height:15.3px;color:var(--ink)}

  .footer__addr{position:absolute;left:28px;top:600px;font-size:7.3px;color:var(--white);display:flex;align-items:center;gap:4px;text-transform:uppercase}
  .footer__contact{position:absolute;right:30px;top:578px;color:var(--white);text-align:right}
  .footer__phone{font-weight:600;font-size:13px;display:flex;align-items:center;justify-content:flex-end;gap:5px}
  .footer__mail{font-size:9.2px;margin-top:3px;display:flex;align-items:center;justify-content:flex-end;gap:5px}

  .whatwedo{left:0;top:269px;width:218px;height:301px;background:var(--copper);border-bottom-right-radius:54px;color:var(--white)}
  .whatwedo h2{position:absolute;left:28px;top:28px;font-size:14px;font-weight:700;letter-spacing:.2px;width:144px;padding-bottom:6px;border-bottom:1px solid rgba(255,255,255,.8)}
  .whatwedo .body-copy{position:absolute;left:30px;top:60px;width:144px;color:var(--white)}
  .whatwedo .callout{position:absolute;left:29px;top:193px;width:150px;border-left:2px solid var(--white);padding-left:11px;font-weight:600;font-size:10.9px;line-height:13.3px}

  .benefit-icon{position:absolute;left:200px;width:35px;height:35px;background:var(--navy);border-radius:8px;display:flex;align-items:center;justify-content:center;box-shadow:0 0 0 3px var(--white)}
  .benefit-icon svg{width:20px;height:20px}
  .benefit{position:absolute;left:243px;width:202px}
</style>
</head>
<body>

<section class="flyer flyer--front">
  <svg class="shapes" viewBox="0 0 484 626" aria-hidden="true">
    <polygon points="0,0 340,0 360,52 0,77" fill="var(--mist)"/>
    <polygon points="190,77 201,77 217,50 206,50" fill="var(--copper)"/>
    <polygon points="307,0 484,0 484,37 332,37" fill="var(--copper)"/>
    <path d="M240,163 V125 A30,30 0 0 1 270,95 H453 V163 Z" fill="var(--blush)"/>
    <path d="M240,163 H453 V262 A40,40 0 0 1 413,302 H240 Z" fill="var(--stone)"/>
    <polygon points="0,589 300,589 276,626 0,626" fill="var(--navy)"/>
    <polygon points="320,569 484,569 484,626 283,626" fill="var(--copper)"/>
  </svg>

  <div class="web" style="top:14px">
    <svg width="7" height="7" viewBox="0 0 10 10"><circle cx="5" cy="5" r="4.2" fill="none" stroke="#fff"/><path d="M1 5h8M5 1c2 2.5 2 5.5 0 8M5 1c-2 2.5-2 5.5 0 8" fill="none" stroke="#fff" stroke-width=".8"/></svg>
    <span>www.<b>brightfenledger</b>.com</span>
  </div>

  <div class="brand" style="left:30px;top:25px">
    <div class="brand__mark"></div>
    <div class="brand__name">Brightfen<br>Ledger Works</div>
  </div>

  <h1 class="abs headline">Experienced<br>Convenient <span>and</span><br>Cost-Effective</h1>
  <p class="abs lede">choice for the accounting and certification needs of companies throughout the country.</p>

  <div class="photo photo--team" role="img" aria-label="Photo of business colleagues around a meeting table"></div>

  <div class="abs services">
    <h2 class="services__title">OUR <b>SERVICES</b></h2>
    <div class="service" style="top:51px">
      <svg viewBox="0 0 20 20" fill="none" stroke="#fff" stroke-width="1.1"><rect x="3" y="4" width="14" height="12" rx="2"/><path d="M3 8h14M7 12h6"/></svg>
      <p>Escrow<br>Reconciliation Services</p>
    </div>
    <div class="service" style="top:80px">
      <svg viewBox="0 0 20 20" fill="none" stroke="#fff" stroke-width="1.1"><rect x="4" y="2" width="12" height="16" rx="1.5"/><path d="M7 7h6M7 10h6M7 13h3"/><circle cx="14" cy="14" r="2.5"/></svg>
      <p>Ledgerline Best<br>Practice Certification</p>
    </div>
    <div class="service" style="top:110px">
      <svg viewBox="0 0 20 20" fill="none" stroke="#fff" stroke-width="1.1"><circle cx="10" cy="7" r="4"/><path d="M3 17c2-3 4-4 7-4s5 1 7 4"/></svg>
      <p>Other<br>Related Services</p>
    </div>
  </div>

  <p class="abs promise">Our knowledge and experience to work for you. We want to help you achieve:</p>
  <div class="abs score">
    <span class="score__num">100%</span>
    <span class="score__list">Compliance<br>Convenience<br>Credibility</span>
  </div>

  <p class="abs body-copy intro">For professionals in the title insurance industry, finding a reliable and cost-effective solution to escrow accounting needs can feel overwhelming. When choosing the right accounting partner, title companies and law firms need a group they can trust, and that’s where we come in. Brightfen Ledger Works is a team that understands the title industry and the importance of compliance, security and accuracy.</p>
  <p class="abs pull">Our team of experienced professionals can be your perfect solution!</p>

  <div class="footer__addr">
    <svg width="6" height="8" viewBox="0 0 6 8"><path d="M3 0a3 3 0 0 1 3 3c0 2-3 5-3 5S0 5 0 3a3 3 0 0 1 3-3z" fill="#fff"/></svg>
    118 Marrow Ct, Fenwick Hollow, CO, 80455, US
  </div>
  <div class="footer__contact">
    <div class="footer__phone">
      <svg width="12" height="12" viewBox="0 0 12 12" fill="none" stroke="#fff" stroke-width="1"><path d="M3 1l1.6 2.4-1 1.2a6 6 0 0 0 3.8 3.8l1.2-1L11 9l-1 2C5 11 1 7 1 2z"/></svg>
      +1 (555) 014-2290
    </div>
    <div class="footer__mail">
      <svg width="9" height="7" viewBox="0 0 9 7" fill="none" stroke="#fff" stroke-width=".8"><rect x=".5" y=".5" width="8" height="6"/><path d="M.5.5l4 3.5 4-3.5"/></svg>
      info@brightfenledger.com
    </div>
  </div>
</section>

<section class="flyer flyer--back">
  <svg class="shapes" viewBox="0 0 484 626" aria-hidden="true">
    <rect x="0" y="0" width="310" height="4" fill="var(--copper)"/>
    <polygon points="299,0 484,0 484,26 318,26" fill="var(--navy)"/>
    <polygon points="0,589 300,589 276,626 0,626" fill="var(--navy)"/>
    <polygon points="320,569 484,569 484,626 283,626" fill="var(--copper)"/>
  </svg>

  <div class="web" style="top:9px">
    <svg width="7" height="7" viewBox="0 0 10 10"><circle cx="5" cy="5" r="4.2" fill="none" stroke="#fff"/><path d="M1 5h8M5 1c2 2.5 2 5.5 0 8M5 1c-2 2.5-2 5.5 0 8" fill="none" stroke="#fff" stroke-width=".8"/></svg>
    <span>www.<b>brightfenledger</b>.com</span>
  </div>

  <div class="brand" style="left:26px;top:24px">
    <div class="brand__mark" style="width:20px;height:20px"></div>
    <div class="brand__name" style="font-size:10px;line-height:11px">Brightfen<br>Ledger Works</div>
  </div>

  <div class="photo photo--desk" role="img" aria-label="Photo of a hand with a pen reviewing a printed ledger beside a laptop"></div>

  <div class="abs whatwedo">
    <h2>WHAT WE DO:</h2>
    <p class="body-copy">Escrow reconciliation services are the core of our business. Let us deliver you peace of mind. When you partner with Brightfen, you know your escrow accounting is secure, accurate and compliant with industry regulations and Best Practices.</p>
    <p class="callout">Since every office operates differently, contact us today for an individualized rate quote for escrow account reconciliation services!</p>
  </div>

  <div class="benefit-icon" style="top:319px">
    <svg viewBox="0 0 20 20" fill="none" stroke="#fff" stroke-width="1.3"><path d="M3 7h13l-3-3M17 13H4l3 3"/></svg>
  </div>
  <p class="abs body-copy benefit" style="top:324px">Daily two-way reconciling is a requirement for Best Practice Certification.</p>

  <div class="benefit-icon" style="top:366px">
    <svg viewBox="0 0 20 20" fill="none" stroke="#fff" stroke-width="1.2"><rect x="3" y="4" width="11" height="8" rx="1"/><path d="M8 12v3M5 15h6"/><rect x="11" y="9" width="6" height="7" rx="1"/></svg>
  </div>
  <p class="abs body-copy benefit" style="top:366px">Regardless of your accounting software system, we can access your network via a secure remote connection.</p>

  <div class="benefit-icon" style="top:429px">
    <svg viewBox="0 0 20 20" fill="none" stroke="#fff" stroke-width="1.2"><rect x="4" y="2" width="12" height="16" rx="1.5"/><path d="M7 6h6M7 15v-3M10 15v-5M13 15v-4"/></svg>
  </div>
  <p class="abs body-copy benefit" style="top:421px">Comprehensive daily and monthly reports will be delivered securely to you, along with a clear breakdown of items that may need your attention.</p>

  <div class="benefit-icon" style="top:491px">
    <svg viewBox="0 0 20 20" fill="none" stroke="#fff" stroke-width="1.2"><circle cx="9" cy="10" r="6"/><path d="M11 8c-.5-1-3.5-1-3.5.6S11 10 11 11.6 8 13 7 12M9 6.5v7"/><path d="M16 11v5M14 14l2 2 2-2"/></svg>
  </div>
  <p class="abs body-copy benefit" style="top:490px">With our low, affordable rates, your company can get a big boost in efficiency with minimal investment.</p>

  <div class="footer__addr">
    <svg width="6" height="8" viewBox="0 0 6 8"><path d="M3 0a3 3 0 0 1 3 3c0 2-3 5-3 5S0 5 0 3a3 3 0 0 1 3-3z" fill="#fff"/></svg>
    118 Marrow Ct, Fenwick Hollow, CO, 80455, US
  </div>
  <div class="footer__contact">
    <div class="footer__phone">
      <svg width="12" height="12" viewBox="0 0 12 12" fill="none" stroke="#fff" stroke-width="1"><path d="M3 1l1.6 2.4-1 1.2a6 6 0 0 0 3.8 3.8l1.2-1L11 9l-1 2C5 11 1 7 1 2z"/></svg>
      +1 (555) 014-2290
    </div>
    <div class="footer__mail">
      <svg width="9" height="7" viewBox="0 0 9 7" fill="none" stroke="#fff" stroke-width=".8"><rect x=".5" y=".5" width="8" height="6"/><path d="M.5.5l4 3.5 4-3.5"/></svg>
      info@brightfenledger.com
    </div>
  </div>
</section>

</body>
</html>
```